We need a full corporate logo and stationary design for our business oxForge. OxForge provides 3D Printing Services to the Australian Market.

Our predominant market is the Mining and Architectural industries and our secondary market is the Entrepreneur / Start-up sector.

What we are after:

1. Logo
2. Business Card Design
3. Letterhead Design
4. Email Signature Design

File Formats we require in colour, greyscale and Black and White:

1 .AI
2 .EPS
3 .TIF
4 .PDF
5 .PNG (300 dpi)
6 .JPG (300 dpi)
7 .GIF (300 dpi)

• Should Not Have:
- "Clip-Art" should not be used.

```html
<!DOCTYPE html>
<html lang="en">
<head>
<meta charset="utf-8">
<title>oxForge Australia – Stationery</title>
<link rel="stylesheet" href="https://fonts.googleapis.com/css2?family=Cinzel:wght@400;700&display=swap">
<style>
  :root {
    --navy: #2e4060;
    --paper: #f2f2f2;
    --ink: #1a1a1a;
    --black-band: #222222;
    --stage: #a8a8a8;
    --silver: #c9c9c9;
    --soft-ink: #555a66;
  }
  * { box-sizing: border-box; margin: 0; padding: 0; }
  html, body { width: 1200px; height: 1000px; overflow: hidden; }
  body {
    position: relative;
    background: linear-gradient(90deg, #a4a4a4 0%, #b0b0b0 60%, #c4c4c4 100%);
    font-family: "Cinzel", "Times New Roman", serif;
    color: var(--ink);
  }
  .piece { position: absolute; background: var(--paper); overflow: hidden; }
  .piece--navy { background: var(--navy); color: #fff; }

  .brand { position: absolute; display: flex; align-items: center; }
  .brand__mark { background: var(--navy); flex: none; }
  .brand__rule { background: var(--navy); flex: none; }
  .brand__name { white-space: nowrap; line-height: 1; }
  .brand__tag { white-space: nowrap; line-height: 1.2; }
  .stack { display: flex; flex-direction: column; }

  .small-caps-line { position: absolute; white-space: nowrap; font-size: 7px; letter-spacing: .2px; }
  .rule { position: absolute; background: var(--navy); }

  .folder { left: 41px; top: 55px; width: 362px; height: 306px; background: #f4f4f4; }
  .folder__band { position: absolute; left: 0; bottom: 0; width: 100%; height: 72px; background: var(--black-band); color: #fff; }

  .letterhead { left: 506px; top: 0; width: 341px; height: 531px; }
  .letterhead-back { left: 863px; top: 0; width: 337px; height: 531px; }
  .watermark { position: absolute; font-size: 46px; color: #e4e4e4; white-space: nowrap; }

  .envelope { left: 249px; top: 561px; width: 460px; height: 205px; }
  .envelope__tab { position: absolute; left: 0; top: 8px; width: 58px; height: 70px; background: #d2d2d2; }
  .envelope-back { left: 737px; top: 561px; width: 462px; height: 205px; }
  .envelope-back__flap { position: absolute; left: 0; top: 0; width: 100%; height: 46px; background: var(--navy); }

  .card { left: 14px; top: 723px; width: 225px; height: 117px; }
  .card-back { left: 15px; top: 881px; width: 225px; height: 116px; }

  .signature { left: 660px; top: 823px; width: 485px; height: 153px; }
  .social { position: absolute; display: flex; gap: 7px; }
  .social__item { display: flex; align-items: center; gap: 3px; font-size: 6px; color: var(--navy); white-space: nowrap; }
  .social__square { width: 12px; height: 12px; background: var(--navy); flex: none; }
</style>
</head>
<body>

  <section class="piece folder">
    <div class="brand" style="left:18px; top:93px;">
      <div class="brand__mark" style="width:26px; height:26px; margin-right:88px;"></div>
      <div class="brand__rule" style="width:4px; height:66px; margin-right:8px;"></div>
      <div class="stack">
        <span class="brand__name" style="font-size:20px;">oxForge Australia</span>
        <span class="brand__tag" style="font-size:12px; margin-top:5px; padding-left:22px;">"Shape it. Forge it."</span>
      </div>
    </div>
    <div class="folder__band">
      <div class="stack" style="position:absolute; left:136px; top:26px; align-items:center;">
        <span class="brand__name" style="font-size:17px;">oxForge Australia</span>
        <span class="brand__tag" style="font-size:9px; margin-top:2px;">"Shape it. Forge it."</span>
      </div>
    </div>
  </section>

  <section class="piece letterhead">
    <div class="brand" style="left:68px; top:16px;">
      <div class="brand__mark" style="width:14px; height:14px; margin-right:62px;"></div>
      <div class="brand__rule" style="width:3px; height:36px; margin-right:5px;"></div>
      <div class="stack">
        <span class="brand__name" style="font-size:11px;">oxForge Australia</span>
        <span class="brand__tag" style="font-size:6px; margin-top:2px;">"Shape it. Forge it."</span>
      </div>
    </div>
    <span class="watermark" style="left:78px; top:240px;">oxForge</span>
    <div class="brand__mark" style="position:absolute; left:158px; top:436px; width:14px; height:14px;"></div>
    <span class="small-caps-line" style="left:102px; top:463px; font-size:8px; color:var(--navy);">3D Printing Services to the Australian</span>
    <div class="rule" style="left:0; top:473px; width:341px; height:3px;"></div>
    <span class="small-caps-line" style="left:82px; top:487px; color:var(--soft-ink);">Level 12 Harbour Lane Sydney, NSW, 2000 &nbsp;&nbsp;&nbsp; Tel: (02) 5550 1234</span>
    <span class="small-caps-line" style="left:100px; top:498px; color:var(--soft-ink);"><b>Fax:</b> (02) 5550 1234 &nbsp;&nbsp;&nbsp; <b>E-mail:</b> hello@oxforge.com.au</span>
  </section>

  <section class="piece piece--navy letterhead-back">
    <div class="brand__mark" style="position:absolute; left:154px; top:30px; width:30px; height:30px; background:var(--silver);"></div>
    <span class="brand__name" style="position:absolute; left:101px; top:86px; font-size:15px;">oxForge Australia</span>
    <div class="brand__mark" style="position:absolute; left:162px; top:436px; width:14px; height:14px; background:var(--silver);"></div>
    <span class="small-caps-line" style="left:98px; top:461px; font-size:8px; color:#d8dce4;">3D Printing Services to the Australian</span>
    <div class="rule" style="left:0; top:471px; width:337px; height:1px; background:#6c7a95;"></div>
    <span class="small-caps-line" style="left:80px; top:482px; font-size:6px; color:#d8dce4;">Level 12 Harbour Lane Sydney, NSW, 2000 &nbsp;&nbsp;&nbsp; Tel: (02) 5550 1234</span>
    <span class="small-caps-line" style="left:100px; top:493px; font-size:6px; color:#d8dce4;">Fax: (02) 5550 1234 &nbsp;&nbsp;&nbsp; E-mail: hello@oxforge.com.au</span>
  </section>

  <section class="piece envelope">
    <div class="envelope__tab">
      <div class="brand__mark" style="position:absolute; left:20px; top:16px; width:16px; height:16px;"></div>
      <span class="brand__name" style="position:absolute; left:9px; top:50px; font-size:5px;">oxForge Australia</span>
    </div>
    <span class="small-caps-line" style="left:6px; top:162px; font-size:7px; color:var(--navy);">3D Printing Services to the Australian</span>
    <div class="rule" style="left:0; top:172px; width:460px; height:3px;"></div>
    <span class="small-caps-line" style="left:8px; top:186px; font-size:5px; color:var(--soft-ink);">Level 12 Harbour Lane Sydney, NSW, 2000</span>
  </section>

  <section class="piece envelope-back">
    <div class="envelope-back__flap">
      <div class="brand__mark" style="position:absolute; left:218px; top:10px; width:24px; height:24px; background:var(--silver);"></div>
    </div>
    <div class="brand__mark" style="position:absolute; left:224px; top:152px; width:12px; height:12px;"></div>
    <div class="rule" style="left:0; top:173px; width:462px; height:3px;"></div>
    <span class="small-caps-line" style="left:158px; top:184px; font-size:7px; color:var(--navy);">3D Printing Services to the Australian</span>
  </section>

  <section class="piece card">
    <div class="brand" style="left:16px; top:16px;">
      <div class="brand__mark" style="width:14px; height:14px; margin-right:58px;"></div>
      <div class="brand__rule" style="width:3px; height:36px; margin-right:5px;"></div>
      <div class="stack">
        <span class="brand__name" style="font-size:10px;">oxForge Australia</span>
        <span class="brand__tag" style="font-size:6px; margin-top:2px;">"Shape it. Forge it."</span>
      </div>
    </div>
    <span class="small-caps-line" style="left:22px; top:78px; font-size:7px; color:var(--navy);">3D Printing Services to the Australian Market.</span>
    <div class="rule" style="left:12px; top:87px; width:205px; height:3px;"></div>
    <span class="small-caps-line" style="left:28px; top:96px; font-size:5px; color:var(--soft-ink);">Level 12 Harbour Lane Sydney, NSW, 2000 &nbsp;&nbsp; Tel: (02) 5550 1234</span>
    <span class="small-caps-line" style="left:52px; top:104px; font-size:5px; color:var(--soft-ink);"><b>Fax:</b> (02) 5550 1234 &nbsp;&nbsp; <b>E-mail:</b> hello@oxforge.com.au</span>
  </section>

  <section class="piece piece--navy card-back">
    <div class="brand__mark" style="position:absolute; left:98px; top:22px; width:28px; height:28px; background:var(--silver);"></div>
    <span class="small-caps-line" style="left:70px; top:84px; font-size:6px; color:#e2e5eb;">www.oxforge.com.au</span>
  </section>

  <section class="piece signature">
    <div class="brand" style="left:16px; top:26px;">
      <div class="brand__mark" style="width:22px; height:22px; margin-right:48px;"></div>
      <div class="brand__rule" style="width:3px; height:44px; margin-right:8px;"></div>
      <div class="stack">
        <span class="brand__name" style="font-size:13px;">oxForge Australia</span>
        <span class="brand__tag" style="font-size:8px; margin-top:3px; padding-left:16px;">"Shape it. Forge it."</span>
      </div>
    </div>
    <div class="rule" style="left:0; top:88px; width:485px; height:3px;"></div>
    <span class="small-caps-line" style="left:16px; top:112px; font-size:8px; color:var(--navy);">Level 12 Harbour Lane Sydney, NSW, 2000</span>
    <span class="small-caps-line" style="left:216px; top:112px; font-size:8px; color:var(--navy);">Tel: (02) 5550 1234</span>
    <span class="small-caps-line" style="left:46px; top:127px; font-size:7px; color:var(--navy);"><b>Fax:</b> (02) 5550 1234 &nbsp;&nbsp;&nbsp;&nbsp; <b>E-mail:</b> hello@oxforge.com.au</span>
    <div class="social" style="left:300px; top:120px;">
      <span class="social__item"><span class="social__square"></span>Friendbook</span>
      <span class="social__item"><span class="social__square"></span>Chirper</span>
      <span class="social__item"><span class="social__square"></span>ViewTube</span>
    </div>
  </section>

</body>
</html>
```